Harbor Nightclub

Nightclub flyer., digital single sided, for KV and PX. I included samples of some previous flyers we've used. Sample Info:
HARBOR
FRIDAYS
FRI MAY 1 2020
DJ VORTAN (club floor)
DJ RUZO & DJ TAV (residents on the lounge floor)
4217 Marlow Avenue Sacramento
www.harborvenuehall.example for list/VIP inquiries

Target Market(s)

Upscale top 40 crowd but want some cool and artsy like the examples included.

Font styles to use
Sans Serif

Requirements
Must have
• Harbor Logo
Nice to have
• Would be nice if the flyer can be incorporated later with DJ photos (sometimes we will add dj photos to pixagram etc). Would like a big city type of feel.
Should not have
• Nothing too sexual.

```html
<!DOCTYPE html>
<html lang="en">
<head>
<meta charset="utf-8">
<title>Harbor Nightclub – Fridays</title>
<link rel="stylesheet" href="https://fonts.googleapis.com/css2?family=Josefin+Sans:wght@300;400&family=Questrial&family=Arimo:wght@400;700&display=swap">
<style>
  :root {
    --ink: #ffffff;
    --ink-soft: rgba(255,255,255,.82);
    --neon: #c73ee6;
    --night-top: #3b1d78;
    --night-blue: #2b2fae;
    --glow-cyan: #3fc6e8;
    --glow-violet: #7b4fd6;
    --haze-pink: #e7c9ec;
    --floor: #1c0b16;
  }
  html, body {
    margin: 0;
    padding: 0;
    overflow: hidden;
    background: var(--floor);
  }
  h1, h2, p { margin: 0; }
  .flyer {
    position: relative;
    width: 962px;
    height: 1200px;
    overflow: hidden;
    color: var(--ink);
    font-family: "Questrial", sans-serif;
  }
  .club-scene {
    position: absolute;
    inset: 0;
    background:
      radial-gradient(ellipse 120px 90px at 905px 290px, rgba(63,198,232,.55), transparent 70%),
      radial-gradient(ellipse 260px 220px at 460px 420px, rgba(63,198,232,.45), transparent 70%),
      radial-gradient(ellipse 230px 110px at 100px 560px, rgba(231,201,236,.75), transparent 75%),
      radial-gradient(ellipse 220px 130px at 860px 520px, rgba(220,220,230,.7), transparent 75%),
      radial-gradient(ellipse 420px 70px at 420px 680px, rgba(120,150,230,.5), transparent 75%),
      radial-gradient(ellipse 320px 120px at 830px 720px, rgba(231,201,236,.35), transparent 75%),
      radial-gradient(ellipse 300px 260px at 640px 250px, rgba(123,79,214,.45), transparent 70%),
      linear-gradient(180deg, var(--night-top) 0%, var(--night-blue) 30%, #3a2a9a 55%, #3a1a5a 72%, #2a1020 85%, var(--floor) 100%);
  }
  .neon-frame {
    position: absolute;
    left: 0;
    top: 0;
  }
  .address {
    position: absolute;
    top: 48px;
    left: 0;
    width: 962px;
    text-align: center;
    font-size: 19px;
    letter-spacing: 12.4px;
    text-indent: 12px;
  }
  .venue-name {
    position: absolute;
    top: 108px;
    left: 0;
    width: 962px;
    text-align: center;
    font-family: "Questrial", sans-serif;
    font-weight: 400;
    font-size: 106px;
    line-height: 106px;
    letter-spacing: 27px;
    text-indent: 27px;
  }
  .night {
    position: absolute;
    top: 706px;
    left: 0;
    width: 962px;
    text-align: center;
    font-family: "Josefin Sans", sans-serif;
    font-weight: 300;
    font-size: 100px;
    line-height: 100px;
    letter-spacing: 6px;
  }
  .date {
    position: absolute;
    top: 814px;
    left: 0;
    width: 962px;
    text-align: center;
    font-family: "Arimo", sans-serif;
    font-size: 30px;
    letter-spacing: 9px;
    text-indent: 9px;
  }
  .headliner {
    position: absolute;
    top: 870px;
    left: 0;
    width: 962px;
    text-align: center;
    font-family: "Arimo", sans-serif;
    font-weight: 700;
    font-size: 120px;
    line-height: 120px;
    letter-spacing: -2px;
  }
  .floor-label {
    position: absolute;
    left: 0;
    width: 962px;
    text-align: center;
    font-family: "Arimo", sans-serif;
    font-size: 15px;
    line-height: 18px;
    letter-spacing: 6px;
    text-indent: 6px;
    color: var(--ink-soft);
  }
  .floor-label.club { top: 986px; }
  .floor-label.lounge { top: 1066px; }
  .residents {
    position: absolute;
    top: 1012px;
    left: 0;
    width: 962px;
    display: flex;
    justify-content: center;
    gap: 62px;
    font-family: "Arimo", sans-serif;
    font-size: 48px;
    line-height: 48px;
  }
  .website {
    position: absolute;
    top: 1122px;
    left: 0;
    width: 962px;
    text-align: center;
    font-size: 26px;
  }
  .venue-mark {
    position: absolute;
    left: 792px;
    top: 1068px;
    width: 112px;
    text-align: center;
  }
  .venue-mark .dot {
    display: block;
    width: 44px;
    height: 44px;
    margin: 0 auto 10px;
    border-radius: 50%;
    background: var(--ink);
  }
  .venue-mark .word {
    font-size: 21px;
    letter-spacing: 1px;
  }
</style>
</head>
<body>
<main class="flyer">
  <div class="club-scene" role="img" aria-label="Blurred nightclub interior in violet and cyan light with soft white clouds drifting across the dance floor"></div>

  <svg class="neon-frame" width="962" height="1200" viewBox="0 0 962 1200" aria-hidden="true">
    <polygon points="445,264 249,539 269,639 767,579" fill="none" stroke="var(--neon)" stroke-width="3" stroke-linejoin="round"/>
  </svg>

  <p class="address">4217 MARLOW AVENUE SACRAMENTO</p>
  <h1 class="venue-name">HARBOR</h1>
  <p class="night">FRIDAYS</p>
  <p class="date">FRI MAY 1 2020</p>
  <h2 class="headliner">DJ VORTAN</h2>
  <p class="floor-label club">CLUB FLOOR</p>
  <p class="residents">
    <span>DJ RUZO</span><span class="divider">|</span><span>DJ TAV</span>
  </p>
  <p class="floor-label lounge">RESIDENTS · LOUNGE FLOOR</p>
  <p class="website">www.harborvenuehall.example</p>
  <div class="venue-mark">
    <span class="dot"></span>
    <span class="word">HARBOR</span>
  </div>
</main>
</body>
</html>
```